Updated Business Card Design more modern and eye catching

looking for something more dynamic than the sterile card we have now. Please take a look at our web site www.brindlemarket.net to see what we do. only looking for the front side of the card for now. I've also attached a sample of a card with raised spot uv ink - it might be cool to incorporate something like that. Card should be bold yet serious. No frilly or scrolly stuff on it.
Updates
Target Market(s)
We do decor and signage for retail business and supermarkets. Our new name should reflect that we're hip but serious.
Contact Information for Business Card
standard business card size - horizontal preferred
Font styles to use
Requirements
Must have
- Current logo and colors cannot be changed.
Nice to have
- Must have information shown on existing card but open to some changes. Okay to consider spot uv.
Should not have
- Not busy with pictures in the background.

```html
<!DOCTYPE html>
<html lang="en">
<head>
<meta charset="UTF-8">
<title>Brindle Market – Business Card Front</title>
<link href="https://fonts.googleapis.com/css2?family=Exo+2:wght@400;600;700&display=swap" rel="stylesheet">
<style>
  :root {
    --backdrop: #c9cbb0;
    --card-white: #ffffff;
    --card-black: #070707;
    --ink: #1a1a1a;
    --gold: #b8a548;
    --title-white: #f2f2f2;
  }
  html, body {
    margin: 0;
    width: 1200px;
    height: 900px;
    overflow: hidden;
    background: var(--backdrop);
    font-family: "Exo 2", sans-serif;
  }
  .card {
    position: absolute;
    left: 75px;
    top: 150px;
    width: 1050px;
    height: 600px;
    background: var(--card-white);
    overflow: hidden;
    box-shadow: 0 12px 30px rgba(0,0,0,0.18);
  }
  .card__field {
    position: absolute;
    inset: 0;
  }
  .brand {
    position: absolute;
    left: 62px;
    top: 64px;
    display: flex;
    align-items: center;
    gap: 16px;
  }
  .brand__square {
    width: 34px;
    height: 34px;
    border: 3px solid var(--ink);
    box-sizing: border-box;
  }
  .brand__name {
    font-weight: 600;
    font-size: 44px;
    letter-spacing: 3px;
    color: var(--ink);
    text-transform: uppercase;
  }
  .address {
    position: absolute;
    left: 62px;
    top: 318px;
    margin: 0;
    font-style: normal;
    font-size: 27px;
    line-height: 36px;
    color: var(--ink);
  }
  .contacts {
    position: absolute;
    left: 62px;
    top: 412px;
    margin: 0;
    padding: 0;
    list-style: none;
    font-size: 29px;
    line-height: 38px;
    color: var(--ink);
  }
  .contacts li {
    display: flex;
    align-items: center;
    gap: 12px;
  }
  .contacts svg {
    width: 24px;
    height: 24px;
    flex: none;
  }
  .person {
    position: absolute;
    right: 70px;
    top: 400px;
    text-align: right;
  }
  .person__name {
    margin: 0;
    font-weight: 700;
    font-size: 36px;
    letter-spacing: 1px;
    color: var(--gold);
    text-transform: uppercase;
  }
  .person__title {
    margin: 2px 0 0;
    font-size: 28px;
    color: var(--title-white);
  }
</style>
</head>
<body>
  <section class="card">
    <svg class="card__field" viewBox="0 0 1050 600" aria-hidden="true">
      <circle cx="900" cy="250" r="390" fill="var(--card-black)"/>
    </svg>

    <div class="brand">
      <span class="brand__square"></span>
      <span class="brand__name">Brindle Market</span>
    </div>

    <address class="address">4170 Harbor Commerce Way<br>Port Alder, FL 34018</address>

    <ul class="contacts">
      <li>
        <svg viewBox="0 0 24 24" fill="none" stroke="var(--ink)" stroke-width="1.8"><rect x="6" y="2" width="12" height="20" rx="2"/><line x1="10" y1="18.5" x2="14" y2="18.5"/></svg>
        555.318.4062
      </li>
      <li>
        <svg viewBox="0 0 24 24" fill="var(--gold)"><path d="M6.6 10.8a15 15 0 0 0 6.6 6.6l2.2-2.2a1 1 0 0 1 1-.25 11.4 11.4 0 0 0 3.6.57 1 1 0 0 1 1 1V20a1 1 0 0 1-1 1A17 17 0 0 1 3 4a1 1 0 0 1 1-1h3.5a1 1 0 0 1 1 1c0 1.25.2 2.45.57 3.57a1 1 0 0 1-.25 1z"/></svg>
        555.207.1190 ext. 3
      </li>
      <li>
        <svg viewBox="0 0 24 24" fill="none" stroke="var(--gold)" stroke-width="1.8"><rect x="2" y="5" width="20" height="14"/><polyline points="2,5 12,13 22,5"/></svg>
        Mara@BrindleMarket.net
      </li>
      <li>
        <svg viewBox="0 0 24 24" fill="none" stroke="var(--gold)" stroke-width="1.6"><circle cx="12" cy="12" r="10"/><ellipse cx="12" cy="12" rx="4.5" ry="10"/><line x1="2" y1="12" x2="22" y2="12"/><line x1="4" y1="7" x2="20" y2="7"/><line x1="4" y1="17" x2="20" y2="17"/></svg>
        www.BrindleMarket.net
      </li>
    </ul>

    <div class="person">
      <p class="person__name">Mara Kellan</p>
      <p class="person__title">Vice-President</p>
    </div>
  </section>
</body>
</html>
```